Gallerine Vault, LLC needs clean, modern business card design

Gallerine Vault is based in Honolulu. We offer fine arts collections management and documentation services for private and corporate art collectors. I would like to use my logo (attached). Card can be either single or double sided and either vertical or horizontal. My clients are businesses with art collections (banks, law firms, etc.) and wealthy individual collectors.

Industry/Entity Type

Business

```html
<!DOCTYPE html>
<html lang="en">
<head>
<meta charset="utf-8">
<title>Gallerine Vault, LLC – Business Card</title>
<link href="https://fonts.googleapis.com/css2?family=Open+Sans:wght@400;600;700&display=swap" rel="stylesheet">
<style>
  :root {
    --sky: #29a8e0;
    --ink: #000000;
    --paper: #ffffff;
    --logo-grey: #8a8a8a;
    --lens: #e4eef5;
    --backdrop: #c9c9c9;
  }
  * { margin: 0; padding: 0; box-sizing: border-box; }
  html, body { width: 1200px; height: 900px; overflow: hidden; }
  body {
    background: var(--backdrop);
    font-family: "Open Sans", Arial, sans-serif;
    position: relative;
  }
  .card {
    position: absolute;
    left: 270px;
    width: 660px;
    height: 377px;
    overflow: hidden;
    background: var(--ink);
  }
  .card--back { top: 40px; }
  .card--front { top: 483px; }

  /* Back side */
  .back-band-top { position: absolute; left: 0; top: 0; width: 100%; height: 72px; background: var(--sky); }
  .back-band-bottom { position: absolute; left: 0; bottom: 0; width: 100%; height: 46px; background: var(--sky); }
  .back-logo {
    position: absolute; left: 0; top: 72px; width: 100%; height: 259px;
    display: flex; align-items: center; justify-content: center; gap: 18px;
  }
  .back-logo .wordmark { color: var(--paper); font-size: 44px; font-weight: 600; letter-spacing: 0.5px; }
  .mark-dot { border-radius: 50%; background: var(--lens); }
  .back-logo .mark-dot { width: 62px; height: 62px; }

  /* Front side */
  .front-top { position: absolute; left: 0; top: 0; width: 100%; height: 150px; }
  .front-logo {
    position: absolute; right: 44px; top: 58px;
    display: flex; align-items: center; gap: 12px;
  }
  .front-logo .wordmark { color: var(--logo-grey); font-size: 30px; font-weight: 600; }
  .front-logo .mark-dot { width: 50px; height: 50px; }
  .front-info { position: absolute; left: 0; top: 150px; width: 100%; height: 196px; background: var(--sky); }
  .person { position: absolute; left: 26px; top: 14px; color: var(--paper); }
  .person-name { font-size: 21px; font-weight: 700; line-height: 1.2; }
  .person-title { font-size: 12px; font-weight: 400; }
  .contact-list {
    position: absolute; right: 24px; top: 62px; list-style: none;
    color: var(--paper); font-size: 15px; line-height: 25px; text-align: right;
  }
  .contact-list li { display: flex; align-items: center; justify-content: flex-end; gap: 10px; white-space: nowrap; }
  .contact-list svg { width: 13px; height: 13px; fill: var(--paper); flex: none; }
  .front-base { position: absolute; left: 0; bottom: 0; width: 100%; height: 31px; background: var(--ink); }
</style>
</head>
<body>

  <section class="card card--back" aria-label="Card back">
    <div class="back-band-top"></div>
    <div class="back-logo">
      <span class="wordmark">Gallerine Vault</span>
      <span class="mark-dot"></span>
    </div>
    <div class="back-band-bottom"></div>
  </section>

  <section class="card card--front" aria-label="Card front">
    <div class="front-top">
      <div class="front-logo">
        <span class="wordmark">Gallerine Vault</span>
        <span class="mark-dot"></span>
      </div>
    </div>
    <div class="front-info">
      <div class="person">
        <p class="person-name">Leilani Kahale</p>
        <p class="person-title">Managing Director</p>
      </div>
      <ul class="contact-list">
        <li>808.555.0142
          <svg viewBox="0 0 16 16" aria-label="Phone"><path d="M2 5c0-2 2-3 6-3s6 1 6 3v1h-3V5H5v1H2z"/><rect x="3" y="7" width="10" height="7" rx="1"/></svg>
        </li>
        <li>808.555.0143
          <svg viewBox="0 0 16 16" aria-label="Fax"><rect x="4" y="1" width="8" height="5"/><rect x="1" y="6" width="14" height="7" rx="1"/><rect x="4" y="11" width="8" height="4"/></svg>
        </li>
        <li>hello@gallerinevault.com
          <svg viewBox="0 0 16 16" aria-label="Email"><path d="M1 3h14v10H1z M2 4l6 5 6-5" fill="none" stroke="#fff" stroke-width="1.6"/></svg>
        </li>
        <li>www.gallerinevault.com
          <svg viewBox="0 0 16 16" aria-label="Website"><g fill="none" stroke="#fff" stroke-width="2"><rect x="1" y="7" width="8" height="5" rx="2.5" transform="rotate(-45 5 9.5)"/><rect x="7" y="4" width="8" height="5" rx="2.5" transform="rotate(-45 11 6.5)"/></g></svg>
        </li>
        <li>1450 Kapiolani Blvd, Honolulu, HI 96814
          <svg viewBox="0 0 16 16" aria-label="Address"><path d="M8 1a5 5 0 0 1 5 5c0 4-5 9-5 9S3 10 3 6a5 5 0 0 1 5-5zm0 3a2 2 0 1 0 0 4 2 2 0 0 0 0-4z"/></svg>
        </li>
      </ul>
    </div>
    <div class="front-base"></div>
  </section>

</body>
</html>
```